依頼詳細
依頼内容は以下の通りです。
・セミナーDMデザイン
・チラシで使用したイラストデータの提供(ホームページやパワーポイントに貼り付け)
・定期的なメンテナンス(2か月に1回程度、日時等の修正依頼予定)
⇒修正依頼する場合、時間的余裕を持って、別途プロジェクト登録します。

参考までに、これまで使用していたデザインと変更依頼内容を添付します。

現行デザインに固執しておりませんので、新たなデザインをお願いしたく思っております。

ご不明点等ございましたら、お問い合わせ下さい。

```html
<!DOCTYPE html>
<html lang="ja">
<head>
<meta charset="utf-8">
<title>コロナ融資借換&資金調達セミナー</title>
<link rel="stylesheet" href="https://fonts.googleapis.com/css2?family=Noto+Sans+JP:wght@400;700;900&family=Dela+Gothic+One&display=swap">
<style>
:root{
  --navy:#1b2f6e;
  --blue:#2f5fb3;
  --sky:#cfe6f7;
  --red:#e0232b;
  --yellow:#ffe100;
  --white:#ffffff;
  --pale:#eef2f7;
  --ink:#222;
  --orange:#f39a1e;
}
*{margin:0;padding:0;box-sizing:border-box}
html,body{width:855px;height:1200px;overflow:hidden;background:#fff}
body{font-family:"Noto Sans JP",sans-serif;color:var(--ink)}
.flyer{position:relative;width:855px;height:1200px;overflow:hidden;background:var(--white)}

.hero-art{position:absolute;left:0;top:0;width:855px;height:380px;
  background:linear-gradient(160deg,#bfe0f5 0%,#e6f3fb 45%,#9fc9ea 100%)}
.callout{position:absolute;font-weight:900;line-height:1.05}
.worry{left:24px;top:14px;display:flex;flex-direction:column;gap:6px}
.worry span{background:var(--white);color:var(--red);font-size:38px;padding:2px 10px;border:3px solid var(--navy);border-radius:6px;width:max-content}
.worry .small{font-size:26px;border:none;background:none;padding:0 10px;text-shadow:0 0 4px #fff}
.plan{right:40px;top:18px;display:flex;flex-direction:column;align-items:flex-end;gap:10px}
.plan .a{background:var(--white);color:var(--red);font-size:36px;padding:4px 14px;border:3px solid var(--navy)}
.plan .b{background:var(--blue);color:var(--white);font-size:40px;padding:4px 14px}
.recover{position:absolute;right:40px;top:255px;background:var(--yellow);color:var(--navy);
  font-family:"Dela Gothic One",sans-serif;font-size:52px;padding:6px 22px;transform:rotate(-6deg);border:4px solid var(--navy)}

.lead{position:absolute;left:40px;top:355px;background:var(--yellow);color:var(--navy);
  font-weight:900;font-size:30px;padding:2px 14px;transform:skewX(-8deg)}
.ruby{position:absolute;left:300px;top:398px;font-size:15px;font-weight:700;color:var(--navy);letter-spacing:2px}
.title{position:absolute;left:30px;font-family:"Dela Gothic One",sans-serif;color:var(--navy);line-height:1}
.title.l1{top:415px;font-size:82px}
.title.l2{top:500px;font-size:82px}
.title.l2 .amp{color:var(--red);font-size:70px}
.seminar{position:absolute;left:745px;top:395px;width:80px;height:195px;background:var(--red);color:var(--white);
  font-family:"Dela Gothic One",sans-serif;font-size:52px;writing-mode:vertical-rl;text-align:center;line-height:80px;letter-spacing:4px}
.sub{position:absolute;left:0;width:855px;top:585px;text-align:center;font-weight:900;font-size:30px;color:var(--navy)}

.info{position:absolute;left:0;top:630px;width:855px;height:495px;background:var(--pale)}
.rows{position:absolute;left:22px;top:20px;width:580px}
.row{display:flex;align-items:center;gap:14px;margin-bottom:14px}
.label{flex:none;width:74px;height:32px;background:var(--navy);color:var(--white);font-weight:700;font-size:17px;display:flex;align-items:center;justify-content:center;border-radius:3px}
.date{font-family:"Dela Gothic One",sans-serif;color:var(--red);font-size:56px;line-height:1}
.date small{font-size:26px}
.venue b{display:block;font-size:34px;font-weight:900;color:var(--navy);line-height:1.1}
.venue span{font-size:15px}
.fee{font-size:22px;font-weight:700}
.host{font-size:18px;font-weight:700;line-height:1.4}
.tel{display:flex;align-items:center;gap:8px;font-family:"Dela Gothic One",sans-serif;font-size:52px;color:var(--red);line-height:1}
.addr{font-size:15px;margin-left:88px;margin-top:-6px}

.bonus{position:absolute;left:610px;top:14px;width:225px;height:300px;background:var(--white);border:3px solid var(--navy);border-radius:8px}
.bonus-tag{position:absolute;left:-14px;top:-14px;width:78px;height:78px;border-radius:50%;background:var(--orange);color:var(--white);font-weight:900;font-size:18px;display:flex;align-items:center;justify-content:center;text-align:center;line-height:1.1}
.bonus h3{margin:14px 0 0 70px;font-size:24px;font-weight:900;color:var(--navy);line-height:1.1}
.bonus-art{position:absolute;left:14px;top:90px;width:192px;height:150px;background:linear-gradient(135deg,#9ec9e8,#f5d28a);border-radius:4px}
.bonus p{position:absolute;left:10px;right:10px;bottom:12px;font-size:13px;text-align:center;line-height:1.35}

.footnote{position:absolute;left:610px;top:330px;width:225px;font-size:13px;line-height:1.5}
.apply{position:absolute;left:0;top:1125px;width:855px;height:40px;background:var(--navy);color:var(--white);font-size:19px;font-weight:700;display:flex;align-items:center;justify-content:center}
.deadline{position:absolute;left:0;top:1165px;width:855px;height:35px;background:var(--yellow);font-size:18px;font-weight:900;display:flex;align-items:center;justify-content:flex-end;padding-right:30px;color:var(--navy)}
.deadline em{font-style:normal;color:var(--red)}
</style>
</head>
<body>
<div class="flyer">
  <div class="hero-art" role="img" aria-label="悩む経営者と業績回復を喜ぶ経営者のイラスト"></div>
  <div class="callout worry"><span>円安</span><span>物価高</span><span>人手不足</span><span class="small">過剰債務<br>返済開始</span></div>
  <div class="callout plan"><span class="a">経営計画の策定</span><span class="b">資金繰り改善!!</span></div>
  <div class="recover">業績回復!!!</div>

  <div class="lead">脱コロ禍を実現する!!</div>
  <div class="ruby">ゆうしかりかえ　しきんちょうたつ</div>
  <div class="title l1">コロナ融資借換</div>
  <div class="title l2"><span class="amp">&amp;</span>資金調達</div>
  <div class="seminar">セミナー</div>
  <div class="sub">ー 今やるべきことが分かる ー</div>

  <section class="info">
    <div class="rows">
      <div class="row"><span class="label">日時</span><span class="date">4.19<small>(水)</small>・5.11<small>(水)</small></span></div>
      <div class="row"><span class="label">会場</span><div class="venue"><b>洛中ビジネス会館</b><span>京都市下京区中央通一丁目12番</span></div></div>
      <div class="row"><span class="label">参加費</span><span class="fee">税込10,000円　早期お申込特典あり</span></div>
      <div class="row"><span class="label">主催</span><span class="host">経営革新等認定支援機関<br>有限会社 川村経営事務所</span></div>
      <div class="row"><span class="label">TEL</span><span class="tel"><svg width="40" height="40" viewBox="0 0 24 24" aria-hidden="true"><path fill="#e0232b" d="M6.6 10.8a15 15 0 0 0 6.6 6.6l2.2-2.2c.3-.3.7-.4 1-.2 1.1.4 2.3.6 3.6.6.6 0 1 .4 1 1V20c0 .6-.4 1-1 1A17 17 0 0 1 3 4c0-.6.4-1 1-1h3.5c.6 0 1 .4 1 1 0 1.3.2 2.5.6 3.6.1.3 0 .7-.2 1z"/></svg>075-000-1234</span></div>
      <div class="addr">有限会社 川村経営事務所　〒600-0000 京都市西京区桜町1丁目5</div>
    </div>

    <div class="bonus">
      <div class="bonus-tag">早期<br>特典</div>
      <h3>早期<br>お申込特典</h3>
      <div class="bonus-art" role="img" aria-label="特典の冊子2冊の表紙"></div>
      <p>資金調達ガイド冊子と<br>借換チェックシートを進呈</p>
    </div>
    <p class="footnote">お申込み後に会場地図と当日の持ち物をご案内します。</p>
  </section>

  <div class="apply">お申込みは裏面の必要事項をご記入の上、FAXにてお送りください。</div>
  <div class="deadline">締切 4月7日(金)　<em>おトクな早期お申込特典は3月31日(金)まで</em></div>
</div>
</body>
</html>
```